Business Card Design

A modern Thai home styled cooking . theme colors are bright orange, spring green and golden brown.I have my logo but need to be redesign coz just copied it from www. need it like it is but better.

Industry/Entity Type

Cooking

Contact Information for Business Card

Lotus Spoon by Nim(Healthier & Tastier) ,Leo Wongsakul GM, 24870 Birch ave (Rear) Glenmore MD 20477, tel 301 555 0164 , www.lotusspoonbynim.example

```html
<!DOCTYPE html>
<html lang="en">
<head>
<meta charset="utf-8">
<title>Lotus Spoon by Nim – Business Card</title>
<link rel="stylesheet" href="https://fonts.googleapis.com/css2?family=Kaushan+Script&family=Tinos&display=swap">
<style>
  :root {
    --spring-green: #66ff00;
    --lime: #a8d000;
    --gold: #d7a300;
    --bright-orange: #ff6a00;
    --burnt-orange: #c44a10;
    --dark-brown: #2a1410;
    --olive-light: #6f8c1f;
    --olive-dark: #3b4a16;
    --ink: #111111;
    --cream: #fde6d2;
    --badge-orange: #f27a1e;
  }
  html, body {
    margin: 0;
    padding: 0;
    width: 1200px;
    height: 702px;
    overflow: hidden;
    background: #ffffff;
  }
  .card {
    position: relative;
    width: 1200px;
    height: 702px;
    overflow: hidden;
    background: linear-gradient(180deg,
      var(--spring-green) 0%,
      var(--lime) 18%,
      var(--gold) 36%,
      var(--bright-orange) 55%,
      var(--burnt-orange) 70%,
      var(--dark-brown) 100%);
  }
  .card__wave {
    position: absolute;
    inset: 0;
    width: 1200px;
    height: 702px;
  }
  .brand-name {
    position: absolute;
    left: 0;
    width: 1215px;
    top: 300px;
    margin: 0;
    text-align: center;
    font-family: "Kaushan Script", cursive;
    font-weight: 400;
    font-size: 92px;
    line-height: 1;
    color: var(--ink);
  }
  .brand-tagline {
    position: absolute;
    left: 0;
    width: 1195px;
    top: 446px;
    margin: 0;
    text-align: center;
    font-family: "Kaushan Script", cursive;
    font-size: 34px;
    line-height: 1;
    color: var(--ink);
  }
  .contact {
    position: absolute;
    left: 0;
    width: 1250px;
    top: 518px;
    margin: 0;
    text-align: center;
    font-family: "Tinos", "Times New Roman", serif;
    font-size: 19px;
    color: var(--ink);
    font-style: normal;
  }
  .contact__line {
    display: block;
    line-height: 1;
  }
  .contact__line--name { margin-bottom: 20px; }
  .contact__line--address { margin-bottom: 16px; }
  .contact__line--phone { margin-bottom: 6px; }
  .badge {
    position: absolute;
    left: 929px;
    top: 464px;
    width: 244px;
    height: 244px;
    border-radius: 50%;
    background: var(--badge-orange);
    display: flex;
    align-items: center;
    justify-content: center;
    text-align: center;
    font-family: "Kaushan Script", cursive;
    font-size: 34px;
    line-height: 1.15;
    color: var(--cream);
  }
</style>
</head>
<body>
  <main class="card">
    <svg class="card__wave" viewBox="0 0 1200 702" aria-hidden="true">
      <defs>
        <linearGradient id="wave-fill" x1="0" y1="0" x2="1" y2="1">
          <stop offset="0" stop-color="var(--olive-light)"/>
          <stop offset="1" stop-color="var(--olive-dark)"/>
        </linearGradient>
      </defs>
      <path d="M0,632 C250,560 600,482 940,472 C905,560 965,650 1080,702 L0,702 Z" fill="url(#wave-fill)"/>
    </svg>

    <h1 class="brand-name">Lotus Spoon by Nim</h1>
    <p class="brand-tagline">Thai Restaurant</p>

    <address class="contact">
      <span class="contact__line contact__line--name">Lotus Spoon by Nim(Healthier &amp; Tastier)</span>
      <span class="contact__line contact__line--address">Leo Wongsakul GM, 24870 Birch ave (Rear) Glenmore MD 20477</span>
      <span class="contact__line contact__line--phone">tel 301 555 0164</span>
      <span class="contact__line contact__line--web">www.lotusspoonbynim.example</span>
    </address>

    <div class="badge">Lotus Spoon<br>by Nim</div>
  </main>
</body>
</html>
```